KB Rubbish Removal Business Card

Hey,
I need a double sided business card designed for a rubbish removal business based in Australia. Logo is already chosen, similar colours preferred for both sides of the business card.

Details to include:

Front:

KB Rubbish Removal
Darren Holloway
Managing Director
Mobile: 0471 902 146
Email: darren@kbrubbishremoval.com.au
Website: kbrubbishremoval.com.au

Rear:

How did we do?
kbrubbishremoval.com.au/review

```html
<!DOCTYPE html>
<html lang="en">
<head>
<meta charset="utf-8">
<title>KB Rubbish Removal – Business Card</title>
<link rel="stylesheet" href="https://fonts.googleapis.com/css2?family=Montserrat:wght@400;500;600;700&display=swap">
<style>
  :root {
    --backdrop: #b8b8b8;
    --card-white: #f7f7f5;
    --brand-green: #1f8a45;
    --deep-green: #0f7a3d;
    --ink-grey: #5f5f5f;
    --rule-grey: #8a8a8a;
    --accent-yellow: #d6c42a;
    --faint-grey: #e4e4e2;
    --white: #ffffff;
  }
  * { margin: 0; padding: 0; box-sizing: border-box; }
  html, body {
    width: 1200px; height: 801px; overflow: hidden;
    background: var(--backdrop);
    font-family: "Montserrat", sans-serif;
  }
  .stage { position: relative; width: 1200px; height: 801px; }
  .card {
    position: absolute;
    width: 525px; height: 300px;
    border-radius: 3px;
    overflow: hidden;
    box-shadow: 0 14px 30px rgba(0,0,0,0.22);
  }
  /* Front */
  .card--front { left: 70px; top: 100px; background: var(--card-white); }
  .card--front .faint-disc {
    position: absolute; right: -60px; bottom: -70px;
    width: 230px; height: 230px; border-radius: 50%;
    background: var(--faint-grey);
  }
  .brand {
    position: absolute; left: 40px; top: 36px;
    display: flex; align-items: center; gap: 12px;
  }
  .brand__dot { width: 30px; height: 30px; border-radius: 50%; background: var(--brand-green); }
  .brand__name {
    font-weight: 700; font-size: 20px; letter-spacing: 0.02em;
    color: var(--brand-green); text-transform: uppercase;
  }
  .person { position: absolute; left: 40px; top: 150px; width: 360px; }
  .person__name {
    font-weight: 600; font-size: 19px; letter-spacing: 0.12em;
    color: var(--brand-green); text-transform: uppercase;
  }
  .person__role {
    margin-top: 2px;
    font-weight: 400; font-size: 12px; letter-spacing: 0.12em;
    color: var(--ink-grey); text-transform: uppercase;
  }
  .person__rule { margin-top: 10px; height: 1px; background: var(--rule-grey); width: 380px; }
  .contact {
    position: absolute; left: 40px; top: 222px;
    font-size: 10.5px; color: var(--ink-grey);
  }
  .contact__row { display: flex; gap: 36px; }
  .contact__label { color: var(--brand-green); letter-spacing: 0.08em; text-transform: uppercase; }
  .contact__value { font-weight: 600; letter-spacing: 0.04em; }
  .contact__web {
    margin-top: 6px;
    font-weight: 500; font-size: 11.5px; letter-spacing: 0.2em;
    color: var(--brand-green); text-transform: uppercase;
  }
  /* Back */
  .card--back {
    left: 610px; top: 420px;
    background: linear-gradient(160deg, var(--deep-green), var(--brand-green));
    display: flex; flex-direction: column; align-items: center; justify-content: center;
  }
  .card--back .back-dot { width: 40px; height: 40px; border-radius: 50%; background: #3fa24f; margin-bottom: 16px; }
  .back__question {
    font-weight: 700; font-size: 15px; letter-spacing: 0.24em;
    color: var(--white); text-transform: uppercase;
  }
  .back__link {
    margin-top: 8px;
    font-weight: 500; font-size: 15px; letter-spacing: 0.12em;
    color: var(--accent-yellow); text-transform: uppercase;
  }
</style>
</head>
<body>
<main class="stage">
  <section class="card card--front" aria-label="Business card front">
    <div class="faint-disc"></div>
    <div class="brand">
      <span class="brand__dot"></span>
      <span class="brand__name">KB Rubbish Removal</span>
    </div>
    <div class="person">
      <p class="person__name">Darren Holloway</p>
      <p class="person__role">Managing Director</p>
      <div class="person__rule"></div>
    </div>
    <div class="contact">
      <div class="contact__row">
        <p><span class="contact__label">Mobile:</span> <span class="contact__value">0471 902 146</span></p>
        <p><span class="contact__label">Email:</span> <span class="contact__value">darren@kbrubbishremoval.com.au</span></p>
      </div>
      <p class="contact__web">kbrubbishremoval.com.au</p>
    </div>
  </section>

  <section class="card card--back" aria-label="Business card back">
    <span class="back-dot"></span>
    <p class="back__question">How did we do?</p>
    <p class="back__link">kbrubbishremoval.com.au/review</p>
  </section>
</main>
</body>
</html>
```